Swimming Pool Service Website needed!!!

Hi Everyone! Thanks for looking at my contest. I PROMISE to provide excellent feedback during this process.

I am starting a new swimming pool business cleaning company in San Diego, California and would like your help in making it similar to one of these two websites that are already functioning.

http://www.brightmeadowhub.example/services-repair.html

http://tryvelmarktide.example/commercial-pool-cleaning.php

I like these two because they are easy to read, classy, sophisticated and have nice pictures of really clean & clear pools.

I really like the blue on white color format.

I do not have a logo, but the name of my company is HARBORLINE POOL SERVICE.

My tag line is: Water so bright, you'll want to dive right in. (does not need to have the quotes around "in"...maybe just italics for this word IN?) You decide for me.

I would like to have a logo designed that incorporates some sort of easy to read letters. I do not want cursive (handwriting) letters. I thought about having a "reflection" of letters (mirror image), but think that this will be hard to read from far away. Maybe you can surprise me and come up with an idea that works using the a mirror image....but I'm not sure. I was leaning toward plain old BLOCK letters as I think it would be easy to read on my truck.

I would like to have 5 pages on my website:
1) Home
2) About Us (Know Your Poolman) / Why Hire Us
3) Services Offered
4) FAQ's
5) Contact

I am looking for a fully-functioning website (coded). Upon selection of the design winner, I am offering to increase the budget/payment by $100-$125 for the coding of all the pages. So anyone looking at participating in this contest, should be willing and able to provide the coding to the webpages that i've requested.

Target Market(s)

Upper middle-class homeowners who have a pool

Industry/Entity Type

Pool Service

Number of Pages Required

5+ page

Font styles to use
Serif

Colors
0455a3
3276b5
85acd3
85cae6
ffffff
33a6d7
0592cd

Requirements
Must have
• The Home page must have this picture highlighted in the top of the page:
• http://www.dunecrestwaterman.example/
• Must have pictures of some high-end pools. Any that you can find on the internet are wonderful.
• Must have a table on the right of the home page that mentions the service areas that we go to:
• • Carmel Valley (92130)
• • Del Mar (92014)
• • Rancho Santa Fe (92067)
• • Solana Beach (92075)
• • Santaluz (92127)
• • Cardiff (92007)
• • Encinitas (92024)
• • Carlsbad (92009, 92008)
• • La Jolla (92037)
• • Pacific Beach (92109)
• • Mira Mesa (92126)
• • Sorrento Valley (92121)
• • Clairemont (92117)
• • Rancho Bernardo (92127, 92128)
• • Rancho Penasquitos (92129)
• • Poway (92064)
Nice to have
• Maybe incorporate some pictures of some kids (or families) playing in pools on the Why Hire Us page?
• I also like the feel of this website, but posting this page just for reference so you can get a feel more of what I like:
• http://www.ferrovaletide.example/
• I like the FAQ's page from this website. I like how you can click on the question and then it pops up with the answer. http://www.quillbrookaquacare.example/pool-spa-fountain-faqs/

```html
<!DOCTYPE html>
<html lang="en">
<head>
<meta charset="utf-8">
<title>Harborline Pool Service</title>
<link href="https://fonts.googleapis.com/css2?family=Amaranth:wght@400;700&family=Lato:ital,wght@0,400;0,700;1,400&display=swap" rel="stylesheet">
<style>
:root{
  --blue:#0592cd;
  --blue-bright:#33a6d7;
  --navy:#0455a3;
  --text:#444;
  --muted:#777;
  --light-bg:#f4f4f4;
  --footer:#222;
  --white:#fff;
  --line:#d8d8d8;
}
*{margin:0;padding:0;box-sizing:border-box}
html,body{width:1200px;height:2200px;overflow:hidden}
body{font-family:'Lato',sans-serif;color:var(--text);background:var(--white);position:relative}
.wrap{position:relative;width:1200px;height:2200px}

.site-header{position:absolute;top:0;left:0;width:1200px;height:77px;background:var(--white)}
.brand{position:absolute;left:196px;top:22px;display:flex;align-items:center;gap:10px;font-family:'Lato',sans-serif;font-weight:700;font-size:22px;color:var(--navy)}
.brand-dot{width:22px;height:22px;border-radius:50%;background:var(--navy)}
.main-nav{position:absolute;right:232px;top:34px;display:flex;gap:26px;font-size:12.5px;color:#555}

.hero{position:absolute;top:77px;left:0;width:1200px;height:503px;
  background:linear-gradient(160deg,#0a2e7a 0%,#0d4fb0 35%,#1f8fd8 55%,#3fc7e8 70%,#7a5b6a 85%,#b27d6a 100%)}
.hero-tagline{position:absolute;left:182px;top:104px;width:480px;font-family:'Amaranth',sans-serif;font-size:37px;line-height:56px;color:var(--white)}

.why{position:absolute;top:580px;left:0;width:1200px;height:358px;background:var(--white);border-bottom:1px solid var(--line)}
.section-title{font-family:'Lato',sans-serif;font-weight:400;font-size:26px;color:var(--blue);text-align:center}
.why .section-title{position:absolute;top:32px;width:100%}
.why-copy{position:absolute;left:193px;top:112px;width:478px;font-size:11.3px;line-height:22.5px;color:#555}
.why-photo{position:absolute;left:683px;top:105px;width:333px;height:210px;
  background:linear-gradient(180deg,#3cc1ee,#1d8fd4);box-shadow:0 14px 18px -10px rgba(0,0,0,.35)}

.services{position:absolute;top:938px;left:0;width:1200px;height:364px;background:var(--light-bg)}
.services .section-title{position:absolute;top:30px;width:100%}
.services-intro{position:absolute;top:80px;left:240px;width:720px;text-align:center;font-size:13.5px;line-height:26px;color:#666}
.service-cols{position:absolute;top:162px;left:183px;width:840px;display:flex;gap:0}
.service-cols ul{list-style:none;width:285px}
.service-cols li{font-size:11.4px;line-height:26.3px;color:#333;padding-left:14px;position:relative}
.service-cols li::before{content:"»";position:absolute;left:0;top:-1px;font-size:13px}

.testimonial{position:absolute;top:1302px;left:0;width:1200px;height:369px;
  background:linear-gradient(120deg,#1e2c33 0%,#0d3a4a 35%,#0c4a60 60%,#1b2e36 100%);text-align:center;color:var(--white)}
.testimonial h2{position:absolute;top:24px;width:100%;font-weight:400;font-size:26px}
.quote-badge{position:absolute;left:572px;top:96px;width:56px;height:56px;border-radius:50%;background:var(--blue-bright)}
.quote-text{position:absolute;top:168px;left:195px;width:810px;font-style:italic;font-size:16px;line-height:30px}
.quote-name{position:absolute;top:276px;width:100%;font-size:15px;color:var(--blue-bright)}
.quote-role{position:absolute;top:298px;width:100%;font-size:13px;color:var(--blue-bright)}
.dots{position:absolute;top:342px;left:578px;display:flex;gap:3px}
.dots span{width:8px;height:8px;border-radius:50%;background:var(--white)}

.faq-area{position:absolute;top:1671px;left:0;width:1200px;height:379px;background:var(--white)}
.faq{position:absolute;left:184px;top:26px;width:406px}
.faq .section-title,.areas .section-title{margin-bottom:30px}
.faq-item{border-bottom:1px solid var(--line);position:relative;height:36px}
.faq-q{font-size:11.4px;color:#444;line-height:34px}
.faq-toggle{position:absolute;right:0;top:10px;width:22px;height:22px;background:var(--blue-bright);color:var(--white);font-weight:700;font-size:16px;line-height:22px;text-align:center}
.faq-item.open{height:auto;border-bottom:1px solid var(--line)}
.faq-a{font-size:9.6px;line-height:16px;color:#888;padding:10px 0 12px;text-align:justify}
.areas{position:absolute;left:620px;top:26px;width:400px}
.area-cols{display:flex;gap:0;padding-left:16px}
.area-cols ul{list-style:none;width:192px}
.area-cols li{font-size:11.4px;line-height:30px;color:#555;padding-left:16px;position:relative}
.area-cols li::before{content:"»";position:absolute;left:0;top:-1px;font-size:13px}
.area-cols ul:first-child{padding-top:4px}

.site-footer{position:absolute;top:2050px;left:0;width:1200px;height:150px;background:var(--footer);color:var(--white)}
.contact-row{position:absolute;top:26px;left:0;width:100%;display:flex;justify-content:center;align-items:center;gap:0}
.contact-item{display:flex;align-items:center;gap:14px}
.contact-email{font-size:15px;padding-right:30px;border-right:1px solid #555;height:36px}
.contact-phone{font-size:21px;padding-left:30px;height:36px}
.footer-rule{position:absolute;top:72px;left:256px;width:728px;height:1px;background:#444}
.footer-legal{position:absolute;top:90px;width:100%;text-align:center;font-size:11px;line-height:22px}
</style>
</head>
<body>
<div class="wrap">
  <header class="site-header">
    <div class="brand"><span class="brand-dot"></span>Harborline Pools</div>
    <nav class="main-nav"><span>Home</span><span>About Us</span><span>Services Offered</span><span>FAQ's</span><span>Why Hire Us</span><span>Contact</span></nav>
  </header>

  <section class="hero" role="img" aria-label="Photo of a lit infinity pool at dusk with lounge chairs and a stone wall">
    <h1 class="hero-tagline">Water so bright, you'll want to dive right <em>in</em>.</h1>
  </section>

  <section class="why">
    <h2 class="section-title">Why You Need Us</h2>
    <div class="why-copy">
      <p>Protect Your Family's Health and Keep Them Safe</p>
      <p>A swimming pool is a major investment, and pool care is a chore that cannot be neglected.&nbsp; An improperly maintained pool will eventually damage your pool's surface and equipment, costing you thousands of dollars to repair or replace.</p>
      <p>Many pool owners are unaware that incorrect pool chemistry can turn pool water into a severe health hazard and can possibly make you ill.&nbsp; While we always take care to keep your pool spotless and beautiful, we also clean up what you can't see.&nbsp; Our focus on and specialized knowledge of water health and safety prevents the growth of dangerous micro-organisms and bacteria that can make your family and guests seriously ill.</p>
    </div>
    <div class="why-photo" role="img" aria-label="Photo of children in swim goggles playing in a clear blue pool"></div>
  </section>

  <section class="services">
    <h2 class="section-title">Services Offered</h2>
    <p class="services-intro">Harborline Pool Service is a full service company. We cover the complete spectrum of regular service and repair. From start-ups to restoring swampy pools, repairing or replacing equipment, Harborline does it all.</p>
    <div class="service-cols">
      <ul>
        <li>Swimming Pool and Spa Cleaning</li>
        <li>Install and repair lighting</li>
        <li>New Pool and Spa Start Ups</li>
        <li>Leak Detection Salt System Conversions</li>
        <li>Troubleshoot and Repair pumps, filters,heaters</li>
        <li>Fountain Cleaning and Service</li>
      </ul>
      <ul>
        <li>Tile Cleaning &amp; Restoration</li>
        <li>Licensed and Bonded Swimming Pool Technicians</li>
        <li>CPO (Certified Pool Operator) Insured</li>
        <li>Low Rates for Repairs, Maintenance, Cleaning</li>
        <li>Reliable and affordable pool and spa maintenance</li>
        <li>Friendly assistance from the staff</li>
      </ul>
      <ul>
        <li>Brushing walls and tile cleaning</li>
        <li>Salt water system maintenance</li>
        <li>Pool leakage detection and repairs</li>
        <li>Noisy pool motor repairs</li>
        <li>Prompt swimming pool cleaning each week</li>
        <li>Vacuuming pool floor and steps</li>
      </ul>
    </div>
  </section>

  <section class="testimonial" role="img" aria-label="Dim photo of a terrace pool at night behind the testimonial">
    <h2>Testrimonial</h2>
    <div class="quote-badge">
      <svg width="56" height="56" viewBox="0 0 56 56"><g fill="#fff"><circle cx="22" cy="29" r="5"/><path d="M17 29 Q17 20 25 18 L25 21 Q20 23 20 29Z"/><circle cx="34" cy="29" r="5"/><path d="M29 29 Q29 20 37 18 L37 21 Q32 23 32 29Z"/></g></svg>
    </div>
    <p class="quote-text">Working with Theo is terrific.&nbsp; His education and professional background sets him apart from all the other pool cleaners. He has excellent communication with us and he shows up when he says he will.&nbsp; Harborline is the only pool care company I have ever recommended to my friends.</p>
    <p class="quote-name">Dana Ortell</p>
    <p class="quote-role">Client</p>
    <div class="dots"><span></span><span></span><span></span><span></span></div>
  </section>

  <section class="faq-area">
    <div class="faq">
      <h2 class="section-title">FAQ</h2>
      <div class="faq-item open">
        <p class="faq-q">Why do my pool and spa need to be chlorinated?</p>
        <span class="faq-toggle">+</span>
        <p class="faq-a">Pools should be disinfected continuously by a chemical which imparts a residual effect. Chlorine is a type of "disinfectant", also called a "sanitizer". Disinfects or sanitizers destroy living microorganisms and bacteria, preventing the transmission of disease. There are several types of disinfectants, such as chlorine, bromine, salt chlorination, ozone, and UV light. Pools need a disinfectant with a measurable residual.</p>
      </div>
      <div class="faq-item"><p class="faq-q">Why do my pool and spa need to be chlorinated?</p><span class="faq-toggle">+</span></div>
      <div class="faq-item"><p class="faq-q">Why do my pool and spa need to be chlorinated?</p><span class="faq-toggle">+</span></div>
      <div class="faq-item"><p class="faq-q">Why do my pool and spa need to be chlorinated?</p><span class="faq-toggle">+</span></div>
    </div>
    <div class="areas">
      <h2 class="section-title">Service Areas</h2>
      <div class="area-cols">
        <ul>
          <li>Carmel Valley (92130)</li>
          <li>Del Mar (92014)</li>
          <li>Rancho Santa Fe (92067)</li>
          <li>Solana Beach (92075)</li>
          <li>Santaluz (92127)</li>
          <li>Cardiff (92007)</li>
          <li>Encinitas (92024)</li>
          <li>Carlsbad (92009, 92008)</li>
        </ul>
        <ul>
          <li>La Jolla (92037)</li>
          <li>Pacific Beach (92109)</li>
          <li>Mira Mesa (92126)</li>
          <li>Sorrento Valley (92121)</li>
          <li>Clairemont (92117)</li>
          <li>Rancho Bernardo (92127, 92128)</li>
          <li>Rancho Penasquitos (92129)</li>
          <li>Poway (92064)</li>
        </ul>
      </div>
    </div>
  </section>

  <footer class="site-footer">
    <div class="contact-row">
      <div class="contact-item contact-email">
        <svg width="34" height="24" viewBox="0 0 34 24"><rect x="1" y="1" width="32" height="22" rx="2" fill="#fff"/><path d="M2 3 L17 14 L32 3" fill="none" stroke="#222" stroke-width="2"/></svg>
        <span>info@harborlinepools.example</span>
      </div>
      <div class="contact-item contact-phone">
        <svg width="26" height="26" viewBox="0 0 24 24"><path fill="#fff" d="M6.6 10.8c1.4 2.8 3.8 5.1 6.6 6.6l2.2-2.2c.3-.3.7-.4 1-.2 1.1.4 2.3.6 3.6.6.6 0 1 .4 1 1V20c0 .6-.4 1-1 1C10.6 21 3 13.4 3 4c0-.6.4-1 1-1h3.5c.6 0 1 .4 1 1 0 1.3.2 2.5.6 3.6.1.3 0 .7-.2 1z"/></svg>
        <span>(858) 555-0147</span>
      </div>
    </div>
    <div class="footer-rule"></div>
    <div class="footer-legal">
      <p>LA &amp; San Fernando Valley Swimming Pool Service © 1995-2015 Tidewell Pool Service. All Rights Reserved</p>
      <p>2210 Marlow Ave.&nbsp; /&nbsp; Suite 118&nbsp; /&nbsp; Sherman Oaks, CA 91403</p>
    </div>
  </footer>
</div>
</body>
</html>
```